Website Redesign - Glow Packs (2 - Pages)

We want a new website that is improved from our first website. Here is an example of a better website: http://www.gleamforte.example/
See our logo attached for design start.
Page 1:
We want a website that looks as good as this but want the following features:
- Top Bar with following Text: Whitening Kits, Whitening Pens, Pura Pulse, Pura Bristle, Accessories & Refills, Instructions, Contact Us
- Right Justified @ top My Account, Checkout
- Static top page image with our ultimate kit photo (attached: Glow Packs - Ultimate Kit.jpg) and an "Order Now" yellow button on the page (See www.velmoraharvest.example for example)
- Five Categories (Teeth Whitening Kits, Teeth Whitening Pens, Pura Pulse, Pura Bristle, Accessories & Refills) all accompanied with pictures and a text bar with name at bottom of pictures... Pura Pulse is a sonic facial brush (don't currently have picture, a filler picture is fine). Pura Bristle is an electronic tooth brush (again don't have product photo)
- Three Pictures Side by Side Pictures to explain product "Save Money", "Whiten Like a Dentist", "Fast Results" (See www.dazzlora.example under why dazz lora with three photos)...
- Reviews ("I love this product!!!", "Works great. Took only 3 sessions to a great smile", "It worked exactly as I had hoped and was simple to use")
- Bottom Order Now Bar (Again, see www.dazzlora.example bottom of page)
Page 2:
Take the instructions and make them part of a cohesive easy to follow page. See Instructions 1, 2, 3

```html
<!DOCTYPE html>
<html lang="en">
<head>
<meta charset="utf-8">
<title>Instructions – Glow Packs</title>
<link href="https://fonts.googleapis.com/css2?family=Open+Sans:wght@400;600;700&family=Source+Sans+3:wght@400;600&display=swap" rel="stylesheet">
<style>
:root{
  --header-blue:#0b68a6;
  --header-dark:#0a5a91;
  --nav-top:#3ea0e0;
  --nav-bottom:#1c7fc6;
  --nav-divider:#1566a3;
  --title-blue:#1f6fb0;
  --ink:#333;
  --muted:#555;
  --tab-grey:#e6e6e6;
  --tab-text:#555;
  --panel-border:#cfcfcf;
  --illus-light:#fafbfc;
  --illus-dark:#dfe4ea;
  --cta-top:#6f7f97;
  --cta-bottom:#4c5b74;
  --footer:#34425a;
  --button-yellow:#f7e98a;
  --button-text:#8a6d10;
}
*{box-sizing:border-box;margin:0;padding:0}
html,body{width:1024px;height:1200px;overflow:hidden}
body{position:relative;background:#fff;font-family:"Open Sans",sans-serif;color:var(--ink)}
.abs{position:absolute}

.site-header{left:0;top:0;width:1024px;height:64px;background:var(--header-blue)}
.brand{left:152px;top:15px;font-size:22px;font-weight:400;color:#fff;letter-spacing:.5px}
.account-link{display:flex;align-items:center;gap:8px;font-size:10px;font-weight:700;color:#fff;top:20px}
.account-link .badge{width:28px;height:28px;border-radius:50%;background:var(--header-dark);display:flex;align-items:center;justify-content:center}
.my-account{left:648px}
.cart{left:778px}

.main-nav{left:0;top:64px;width:1024px;height:32px;background:linear-gradient(var(--nav-top),var(--nav-bottom));border-bottom:1px solid #d8e6f1}
.main-nav ul{list-style:none;position:absolute;left:127px;top:0;display:flex;height:32px;border-left:1px solid var(--nav-divider)}
.main-nav li{height:32px;display:flex;align-items:center;justify-content:center;color:#fff;font-family:"Source Sans 3",sans-serif;font-size:13.5px;border-right:1px solid var(--nav-divider)}

.page-title{left:0;width:1024px;top:122px;text-align:center;font-size:19px;font-weight:400;color:var(--title-blue)}
.page-intro{left:0;width:1024px;top:156px;text-align:center;font-size:10px;color:var(--muted)}

.tab{top:194px;height:32px;display:flex;align-items:center;justify-content:center;font-size:12px;font-weight:700;color:var(--tab-text);background:var(--tab-grey);border:1px solid #d4d4d4;border-bottom:none}
.tab.active{background:linear-gradient(#48a8e6,#1a7cc2);color:#fff;border-color:#1a7cc2}

.step-panel{left:136px;top:226px;width:751px;height:836px;border:1px solid var(--panel-border);background:#fff}
.panel-heading{left:0;width:1024px;top:253px;text-align:center;font-size:19px;font-weight:600;color:#444}
.illustration{background:radial-gradient(ellipse at 50% 55%,var(--illus-light) 0%,#eef1f4 55%,var(--illus-dark) 100%);border-radius:4px}
.caption{text-align:center;font-family:"Source Sans 3",sans-serif;font-size:18.5px;line-height:24px;color:#222}

.cta-band{left:0;top:1086px;width:1024px;height:76px;background:radial-gradient(ellipse 180px 60px at 560px 0,#a9b4c5,transparent),linear-gradient(var(--cta-top),var(--cta-bottom))}
.cta-heading{left:248px;top:1101px;font-size:24px;font-weight:700;color:#fff;letter-spacing:.5px}
.cta-sub{left:249px;top:1133px;font-size:10px;color:#b4c0d2;letter-spacing:.3px}
.order-button{left:634px;top:1110px;width:141px;height:34px;background:linear-gradient(#fbf2a8,var(--button-yellow));border:1px solid #e4d36a;border-radius:2px;display:flex;align-items:center;justify-content:center;font-size:12.5px;font-weight:700;letter-spacing:1.2px;color:var(--button-text)}

.site-footer{left:0;top:1162px;width:1024px;height:38px;background:var(--footer);border-top:1px solid #56637a}
.footer-text{top:1175px;font-family:"Source Sans 3",sans-serif;font-size:10.5px;color:#e5e9ef}
</style>
</head>
<body>

<header class="site-header abs"></header>
<div class="brand abs">Glow Packs</div>
<div class="account-link my-account abs">
  <span class="badge"><svg width="14" height="14" viewBox="0 0 14 14"><circle cx="7" cy="4" r="3" fill="#fff"/><path d="M1.5 13c0-3.2 2.5-5 5.5-5s5.5 1.8 5.5 5z" fill="#fff"/></svg></span>MY ACCOUNT
</div>
<div class="account-link cart abs">
  <span class="badge"><svg width="15" height="14" viewBox="0 0 15 14"><path d="M1 1.5h2.2l1.6 7.5h7.2l1.5-5.5H4" fill="none" stroke="#fff" stroke-width="1.6"/><circle cx="5.5" cy="11.8" r="1.3" fill="#fff"/><circle cx="11" cy="11.8" r="1.3" fill="#fff"/></svg></span>CART&nbsp;&nbsp;(0)
</div>

<nav class="main-nav abs">
  <ul>
    <li style="width:112px">Whitening Kits</li>
    <li style="width:120px">Whitening Pens</li>
    <li style="width:97px">Pura Pulse</li>
    <li style="width:101px">Pura Bristle</li>
    <li style="width:149px">Accessories &amp; Refills</li>
    <li style="width:99px">Instructions</li>
    <li style="width:90px">Contact Us</li>
  </ul>
</nav>

<h1 class="page-title abs">Instructions</h1>
<p class="page-intro abs">Follow these 4 easy steps so you can get the best whitening results.</p>

<div class="tab active abs" style="left:268px;width:122px">STEP 1</div>
<div class="tab abs" style="left:392px;width:120px">STEP 2</div>
<div class="tab abs" style="left:515px;width:120px">STEP 3</div>
<div class="tab abs" style="left:638px;width:121px">STEP 4</div>

<section class="step-panel abs"></section>
<h2 class="panel-heading abs">Pre-fitting Procedure</h2>

<div class="illustration abs" role="img" aria-label="Line drawing of a pot of water boiling on a gas burner" style="left:256px;top:318px;width:192px;height:224px"></div>
<p class="caption abs" style="left:192px;width:320px;top:564px">1. Set water to boil.</p>

<div class="illustration abs" role="img" aria-label="Line drawing of a whitening tray held by its tab and dipped into hot water" style="left:548px;top:318px;width:192px;height:210px"></div>
<p class="caption abs" style="left:490px;width:320px;top:552px">2. Dip tray by the tab<br>in for 3-4 seconds.<br>(or until the tray starts to soften)</p>

<div class="illustration abs" role="img" aria-label="Line drawing of a person placing the softened tray in the mouth" style="left:256px;top:677px;width:194px;height:200px"></div>
<p class="caption abs" style="left:190px;width:320px;top:900px">3. Place in mouth and<br>suck the air out from tray<br>to fit.</p>

<div class="illustration abs" role="img" aria-label="Line drawing of scissors cutting the tab off the fitted tray" style="left:502px;top:698px;width:268px;height:200px"></div>
<p class="caption abs" style="left:516px;width:320px;top:915px">4. Cut tab off fitted tray.</p>

<section class="cta-band abs"></section>
<div class="cta-heading abs">Get your glow packs TODAY!</div>
<div class="cta-sub abs">If you have any further queries please do not hesitate to contact us.</div>
<div class="order-button abs">ORDER NOW</div>

<footer class="site-footer abs"></footer>
<div class="footer-text abs" style="left:247px">Copyright © 2014 All Rights Reserved.&nbsp; Glow Packs.</div>
<div class="footer-text abs" style="left:606px">Terms and Conditions&nbsp; |&nbsp; Privacy Policy</div>

</body>
</html>
```